Automotive component supplier needs a business card design

We need a business card design for our company called Velmar Global Components Ltd based in the UK. We are a supplier of interior and exterior components to premium car manufacturers such as Corvane Hale, Durrant Fyfe, Maxtorn and Valdessimo. We would like to see a modern business card design that uses the colour blue.

Target Market(s)

Premium automotive car manufacturers.

Industry/Entity Type

Automotive

Contact Information for Business Card

Company Name : Velmar Global Components Limited
Address: 17 Tamsey Yard, Upper Drisk, Warwick, CV31 8RJ, United Kingdom
Web Address : www.velmarparts-example.co.uk

Font styles to use
Other font styles liked:
• Helvetica

Colors
3176b5
0255a3
85acd3
cfdeed
cee9f5
85cae6
34a6d7
0692cd
9bcb3c

Requirements
Must have
• Clear company logo and a mixture of blue colours.
Nice to have
• A high quality modern image.
Should not have
• Multiple colours.

```html
<!DOCTYPE html>
<html lang="en">
<head>
<meta charset="utf-8">
<title>Velmar Global Components – Business Card</title>
<link rel="stylesheet" href="https://fonts.googleapis.com/css2?family=Roboto:wght@300;400;700&display=swap">
<style>
  :root {
    --page: #e8ecec;
    --paper: #ffffff;
    --charcoal: #343b43;
    --lime: #9bcb3c;
    --lime-soft: #cfe5a6;
    --brand-blue: #0692cd;
    --ink: #2f3337;
  }
  html, body {
    margin: 0;
    width: 1198px;
    height: 1200px;
    overflow: hidden;
    background: var(--page);
    font-family: "Roboto", Helvetica, Arial, sans-serif;
  }
  .card {
    position: absolute;
    width: 686px;
    height: 438px;
    box-shadow: 0 22px 18px -14px rgba(0,0,0,0.35);
  }
  .card svg.card-shapes {
    position: absolute;
    inset: 0;
    width: 100%;
    height: 100%;
  }
  .card-front { left: 120px; top: 120px; background: var(--paper); }
  .card-back { left: 392px; top: 641px; background: var(--charcoal); }

  .text { position: absolute; white-space: nowrap; line-height: 1; }

  .wordmark {
    left: 58px; top: 58px;
    display: flex; align-items: center; gap: 10px;
  }
  .wordmark-dot { width: 12px; height: 12px; background: var(--lime); }
  .wordmark-name {
    font-weight: 700; font-size: 25px; color: var(--brand-blue);
  }

  .person { left: 542px; top: 148px; transform: translateX(-50%); text-align: center; color: var(--ink); }
  .person-name { font-weight: 700; font-size: 26px; }
  .person-title { font-weight: 400; font-size: 20px; margin-top: 5px; }

  .address { left: 33px; top: 292px; font-size: 20px; color: var(--ink); line-height: 25px; }
  .web-front { left: 33px; top: 384px; font-size: 17px; color: #fff; }

  .contact { font-size: 20px; color: #fff; }
  .phone { left: 395px; top: 313px; }
  .mobile { left: 385px; top: 348px; }
  .email { left: 375px; top: 381px; font-size: 19px; }

  .wordmark-back {
    left: 50%; top: 204px; transform: translateX(-50%);
    display: flex; align-items: center; gap: 12px;
  }
  .wordmark-back .wordmark-name { color: #fff; font-size: 30px; }

  .web-back {
    left: 50%; top: 377px; transform: translateX(-50%);
    font-size: 18px; letter-spacing: 4px; color: #fff; font-weight: 300;
  }
  .web-back .accent { color: var(--lime); font-weight: 700; }
</style>
</head>
<body>

<section class="card card-front" aria-label="Business card front">
  <svg class="card-shapes" viewBox="0 0 858 548" aria-hidden="true">
    <polygon points="585,0 858,0 858,52 566,52" fill="var(--charcoal)"/>
    <polygon points="558,74 858,74 858,340 465,340" fill="var(--lime)"/>
    <polygon points="455,364 858,364 858,548 392,548" fill="var(--charcoal)"/>
    <polygon points="0,468 365,468 347,514 0,514" fill="var(--lime)"/>
    <polygon points="368,468 380,468 362,514 350,514" fill="var(--lime-soft)"/>
    <g class="tag-phone">
      <polygon points="441,386 478,386 470,420 434,420" fill="var(--lime)"/>
      <path d="M445,398 q9,-7 18,0 l-2,4 h-3 l-1,-2 h-6 l-1,2 h-3 z M449,403 h10 l2,8 h-14 z" fill="#fff"/>
      <circle cx="454" cy="407" r="2" fill="var(--lime)"/>
    </g>
    <g class="tag-mobile">
      <polygon points="426,430 462,430 454,464 418,464" fill="var(--lime)"/>
      <rect x="434" y="438" width="11" height="18" rx="1.5" fill="#fff"/>
      <rect x="436" y="440" width="7" height="5" fill="var(--lime)"/>
    </g>
    <g class="tag-email">
      <polygon points="410,473 448,473 440,508 402,508" fill="var(--lime)"/>
      <rect x="414" y="484" width="20" height="13" fill="#fff"/>
      <polyline points="414,484 424,492 434,484" fill="none" stroke="var(--lime)" stroke-width="1.5"/>
    </g>
  </svg>

  <div class="text wordmark">
    <span class="wordmark-dot"></span>
    <span class="wordmark-name">Velmar Global Components</span>
  </div>

  <div class="text person">
    <div class="person-name">Elinor Pashby</div>
    <div class="person-title">Branch Director</div>
  </div>

  <div class="text address">
    17 Tamsey Yard, Upper Drisk<br>
    Warwick, CV31 8RJ<br>
    United Kingdom
  </div>
  <div class="text web-front">www.velmarparts-example.co.uk</div>

  <div class="text contact phone">+44 1926 555 0148</div>
  <div class="text contact mobile">+44 7700 900 362</div>
  <div class="text contact email">hello@velmarparts-example.co.uk</div>
</section>

<section class="card card-back" aria-label="Business card back">
  <div class="text wordmark-back">
    <span class="wordmark-dot"></span>
    <span class="wordmark-name">Velmar Global Components</span>
  </div>
  <div class="text web-back">www.<span class="accent">velmarparts-example</span>.co.uk</div>
</section>

</body>
</html>
```